Pet sitting and Dog Walking Postcard distributed to new home owners in our target market

We need a two-sided postcard (or rack card, size can be anything rack card size or smaller) that is going in a folder that will be distributed each month to new homeowners in our target area. I would like the design to be similar to our brochure which will be uploaded here for you to see. It needs much less information than the brochure.
Should include services we offer; and our 4 systems: online registration, complimentary consultation, flexible scheduling, visits with reports and photos. Should also include our contact information (website, email, phone). Photos from the brochure can be used. Tagline from the cover of the brochure can be used. Call to action should be: Register on our website today to receive a free consultation and $20 off your first booking (when requesting a service, mention the promo code: welcome20).

```html
<!DOCTYPE html>
<html lang="en">
<head>
<meta charset="utf-8">
<title>Paw Haven Pet Care – Rack Card</title>
<link rel="stylesheet" href="https://fonts.googleapis.com/css2?family=Open+Sans:wght@400;600;700;800&family=Raleway:ital,wght@0,400;0,600;0,700;1,400;1,700&display=swap">
<style>
  :root{
    --stage:#1c1b1f;
    --plum:#5b4662;
    --plum-dark:#4a3851;
    --green:#3fa535;
    --green-bright:#4cc23e;
    --white:#ffffff;
    --ink:#3b2f41;
    --photo-warm-a:#d9cbbd;
    --photo-warm-b:#8c7566;
    --photo-light-a:#f3efe9;
    --photo-light-b:#cdbfae;
  }
  *{box-sizing:border-box;margin:0;padding:0}
  html,body{width:1200px;height:1026px;overflow:hidden;background:var(--stage)}
  body{position:relative;font-family:"Raleway",Arial,sans-serif;color:var(--ink)}
  .card{position:absolute;top:72px;width:400px;height:880px;overflow:hidden;box-shadow:0 6px 24px rgba(0,0,0,.45)}
  .card--front{left:170px;background:var(--plum)}
  .card--back{left:630px;background:var(--white)}

  /* front */
  .front-deco{position:absolute;inset:0}
  .brand{position:absolute;left:0;right:0;text-align:center;font-family:"Open Sans",Arial,sans-serif;font-weight:700;color:var(--white)}
  .brand__mark{display:block;width:34px;height:34px;border-radius:50%;background:var(--white);margin:0 auto 8px}
  .brand__name{font-size:17px;letter-spacing:.3px;line-height:1.15}
  .brand__sub{font-size:10px;letter-spacing:3px;font-weight:600}
  .card--front .brand{top:58px}
  .hero-photo{position:absolute;left:38px;top:178px;width:330px;height:330px;border-radius:50%;border:9px solid var(--white);
    background:radial-gradient(circle at 45% 45%,var(--photo-light-a),var(--photo-light-b) 55%,var(--photo-warm-b))}
  .tagline{position:absolute;top:540px;left:0;right:0;text-align:center;font-family:"Open Sans",Arial,sans-serif;font-weight:700;font-size:21px;line-height:1.2}
  .tagline__lead{color:var(--white)}
  .tagline__pets{color:var(--green-bright)}
  .front-footer{position:absolute;left:0;right:0;bottom:0;height:245px;background:var(--white);border-top:5px solid var(--green)}
  .serving{position:absolute;left:22px;top:18px;font-family:"Open Sans",Arial,sans-serif;font-weight:700;font-size:15.5px;line-height:1.2;color:var(--ink)}
  .serving em{font-style:normal;color:var(--green)}
  .phone{display:flex;align-items:center;gap:5px;font-family:"Open Sans",Arial,sans-serif;font-weight:800;color:var(--ink);white-space:nowrap}
  .phone__word{color:var(--green)}
  .phone__icon{flex:none;border-radius:50%;background:var(--green);display:flex;align-items:center;justify-content:center}
  .front-footer .phone{position:absolute;left:20px;top:118px;font-size:26px}
  .front-footer .phone__icon{width:20px;height:20px}
  .contact-line{display:flex;align-items:center;gap:6px;font-family:"Open Sans",Arial,sans-serif;font-weight:600;color:var(--ink)}
  .contact-line::before{content:"";width:9px;height:9px;border-radius:50%;background:var(--green)}
  .front-footer .contacts{position:absolute;left:22px;top:158px;font-size:11.5px;display:grid;gap:4px}
  .dog-photo{position:absolute;background:radial-gradient(ellipse at 50% 40%,#f5eee3,#dcc8a8 60%,#eae6e0)}
  .front-footer .dog-photo{right:12px;top:14px;width:120px;height:165px;border-radius:50% 50% 8px 8px}

  /* back */
  .about{position:absolute;left:20px;top:18px;width:168px;font-size:9px;line-height:1.38;color:var(--ink)}
  .about h2{font-family:"Open Sans",Arial,sans-serif;font-size:15px;color:var(--green);margin-bottom:3px}
  .about strong{font-style:italic}
  .about-photo{position:absolute;right:-20px;top:30px;width:230px;height:230px;border-radius:50%;border:4px solid var(--plum);
    background:radial-gradient(circle at 55% 40%,#f2ebe4,var(--photo-warm-a) 50%,var(--photo-warm-b))}
  .pets-row{position:absolute;left:20px;top:216px;width:140px;height:48px;border-radius:6px;background:linear-gradient(90deg,#e9e0d4,#b79d82,#e5ddd2)}
  .services-panel{position:absolute;left:0;right:0;top:280px;height:510px;background:var(--plum)}
  .services-title{position:absolute;left:18px;top:10px;font-family:"Open Sans",Arial,sans-serif;font-weight:800;font-size:12.5px;color:var(--white)}
  .services-title span{color:var(--green-bright)}
  .services-list{position:absolute;left:18px;top:34px;list-style:none;display:grid;gap:5px}
  .services-list li{display:flex;align-items:center;gap:7px;font-family:"Open Sans",Arial,sans-serif;font-weight:700;font-size:11px;color:var(--white)}
  .service-thumb{width:15px;height:15px;border-radius:50%;border:1.5px solid var(--white);background:radial-gradient(#e8d8c0,#9a7c5e)}
  .services-panel .dog-photo{right:14px;top:6px;width:108px;height:130px;border-radius:50% 50% 6px 6px}
  .ready{position:absolute;left:18px;top:150px;font-family:"Open Sans",Arial,sans-serif;font-weight:700;font-size:14px;color:var(--white)}
  .ready span{color:var(--green-bright)}
  .ready-text{position:absolute;left:18px;right:16px;top:174px;font-size:9px;line-height:1.3;color:var(--white)}
  .systems{position:absolute;left:16px;right:16px;top:226px;list-style:none;display:grid;gap:9px}
  .system{display:grid;grid-template-columns:34px 1fr;gap:10px;align-items:start}
  .system__icon{width:30px;height:30px;border-radius:50%;background:var(--white);display:flex;align-items:center;justify-content:center;margin-top:8px}
  .system h3{font-family:"Open Sans",Arial,sans-serif;font-size:9.5px;color:var(--green-bright);margin-bottom:2px}
  .system p{font-size:8.6px;line-height:1.25;color:var(--white);font-style:italic}
  .offer{position:absolute;left:16px;right:16px;top:420px;padding:10px 14px;border-radius:6px;background:var(--green);color:var(--white);text-align:center;font-family:"Open Sans",Arial,sans-serif}
  .offer__lead{font-weight:800;font-size:12px;line-height:1.3}
  .offer__code{margin-top:4px;font-weight:600;font-size:10px}
  .offer__code strong{display:inline-block;margin-left:3px;padding:1px 7px;border-radius:3px;background:var(--white);color:var(--plum);font-weight:800;letter-spacing:.5px}
  .back-footer{position:absolute;left:0;right:0;bottom:0;height:90px;background:var(--white)}
  .back-footer .brand{left:14px;right:auto;top:10px;width:110px;color:var(--plum)}
  .back-footer .brand__mark{width:22px;height:22px;background:var(--plum);margin-bottom:5px}
  .back-footer .brand__name{font-size:11px}
  .back-footer .brand__sub{font-size:7px;letter-spacing:2px;color:var(--green)}
  .contact-us{position:absolute;right:18px;top:6px;font-family:"Open Sans",Arial,sans-serif;font-weight:700;font-size:13px;color:var(--green)}
  .back-footer .phone{position:absolute;right:18px;top:24px;font-size:22px}
  .back-footer .phone__icon{width:18px;height:18px}
  .back-footer .contacts{position:absolute;right:18px;top:56px;font-size:10.5px;display:grid;gap:1px}
</style>
</head>
<body>

<section class="card card--front" aria-label="Rack card front">
  <svg class="front-deco" width="400" height="880" viewBox="0 0 400 880" aria-hidden="true">
    <path d="M40 40 A190 190 0 0 1 160 160" fill="none" stroke="var(--green)" stroke-width="3"/>
    <path d="M330 20 Q345 80 318 140" fill="none" stroke="var(--green)" stroke-width="3"/>
    <circle cx="203" cy="343" r="180" fill="none" stroke="var(--green)" stroke-width="3" stroke-dasharray="280 850" transform="rotate(-40 203 343)"/>
    <circle cx="203" cy="343" r="180" fill="none" stroke="var(--green)" stroke-width="3" stroke-dasharray="120 1010" transform="rotate(150 203 343)"/>
  </svg>
  <div class="brand">
    <span class="brand__mark"></span>
    <div class="brand__name">PAW HAVEN</div>
    <div class="brand__sub">— PET CARE —</div>
  </div>
  <div class="hero-photo" role="img" aria-label="Smiling woman on a sofa holding a black and white spaniel"></div>
  <p class="tagline"><span class="tagline__lead">Prioritize Yourself.</span><br><span class="tagline__pets">We'll Focus on Your Pets.</span></p>
  <div class="front-footer">
    <p class="serving">Proudly serving<br><em>Brookdale &amp; surrounding</em><br>neighborhoods for<br><em>over 15 years.</em></p>
    <div class="phone">
      <span class="phone__icon"><svg width="11" height="11" viewBox="0 0 24 24"><path fill="#fff" d="M6.6 10.8a15 15 0 0 0 6.6 6.6l2.2-2.2c.3-.3.7-.4 1-.2 1.1.4 2.3.6 3.6.6.6 0 1 .4 1 1V20c0 .6-.4 1-1 1A17 17 0 0 1 3 4c0-.6.4-1 1-1h3.5c.6 0 1 .4 1 1 0 1.3.2 2.5.6 3.6.1.3 0 .7-.2 1z"/></svg></span>
      <span class="phone__number">555-210-<span class="phone__word">BARK</span></span>
    </div>
    <div class="contacts">
      <span class="contact-line">www.pawhavenpets.com</span>
      <span class="contact-line">hello@pawhavenpets.com</span>
    </div>
    <div class="dog-photo" role="img" aria-label="Yellow labrador lying down wearing a blue collar"></div>
  </div>
</section>

<section class="card card--back" aria-label="Rack card back">
  <div class="about-photo" role="img" aria-label="Woman with curly hair hugging an Australian shepherd dog"></div>
  <div class="about">
    <h2>About</h2>
    <p>We specialize in one-to-one personalized, quality pet care. We offer many services to cater to your needs. Whether you have dogs, cats, reptiles or rodents, <strong>we can help!</strong><br>If you have pets and experience any feelings of guilt when you need to leave them behind, reach out to us! We pick right up where you leave off, with smiles, love and adventures that can turn an ordinary day extraordinary!</p>
  </div>
  <div class="pets-row" role="img" aria-label="Row of small dogs and cats sitting together"></div>

  <div class="services-panel">
    <h2 class="services-title">PROFESSIONAL <span>PET CARE SERVICES</span></h2>
    <ul class="services-list">
      <li><span class="service-thumb" role="img" aria-label="Dog thumbnail"></span>Day Care and Overnight Boarding</li>
      <li><span class="service-thumb" role="img" aria-label="Dog thumbnail"></span>Dog Walking</li>
      <li><span class="service-thumb" role="img" aria-label="Dog thumbnail"></span>Sleepovers</li>
      <li><span class="service-thumb" role="img" aria-label="Dog thumbnail"></span>Pet Sitting</li>
      <li><span class="service-thumb" role="img" aria-label="Cat thumbnail"></span>Cat Sitting/Small Pet Sitting</li>
    </ul>
    <div class="dog-photo" role="img" aria-label="Sitting yellow labrador with a blue collar"></div>
    <h2 class="ready">Ready To Free Up <span>Your Time?</span></h2>
    <p class="ready-text">We are here to uncomplicate your life! Our systems and processes allow for seamless scheduling, service and billing. Give us a few minutes of your time and we will deliver it back to you tenfold!</p>
    <ul class="systems">
      <li class="system">
        <span class="system__icon"><svg width="16" height="14" viewBox="0 0 16 14"><rect x="1" y="1" width="14" height="9" rx="1" fill="none" stroke="var(--plum)" stroke-width="1.6"/><path d="M5 13h6M8 10v3" stroke="var(--plum)" stroke-width="1.6"/></svg></span>
        <div><h3>Online Registration</h3><p>Click on the register link on our homepage to begin online registration or submit a request form if you would like more information first.</p></div>
      </li>
      <li class="system">
        <span class="system__icon"><svg width="16" height="14" viewBox="0 0 16 14"><path d="M2 1h12v8H6l-3 3V9H2z" fill="var(--plum)"/></svg></span>
        <div><h3>Complimentary Consultation</h3><p>Click on the register link on our homepage to begin online registration or submit a request form if you would like more information first.</p></div>
      </li>
      <li class="system">
        <span class="system__icon"><svg width="15" height="15" viewBox="0 0 15 15"><rect x="1.5" y="2.5" width="12" height="11" rx="1" fill="none" stroke="var(--plum)" stroke-width="1.6"/><path d="M1.5 6h12M5 1v3M10 1v3" stroke="var(--plum)" stroke-width="1.6"/></svg></span>
        <div><h3>Flexible Scheduling</h3><p>Click on the register link on our homepage to begin online registration or submit a request form if you would like more</p></div>
      </li>
      <li class="system">
        <span class="system__icon"><svg width="16" height="13" viewBox="0 0 16 13"><path d="M1 3h4l1.5-2h3L11 3h4v9H1z" fill="var(--plum)"/><circle cx="8" cy="7.5" r="2.6" fill="#fff"/></svg></span>
        <div><h3>Visits with Reports and Photos</h3><p>Your pets will be cared for by our elite team of Pet Care Specialists. After each visit, you will receive an emailed report with photo.</p></div>
      </li>
    </ul>
    <div class="offer">
      <p class="offer__lead">Register on our website today to receive a free consultation and $20 off your first booking!</p>
      <p class="offer__code">When requesting a service, mention the promo code: <strong>welcome20</strong></p>
    </div>
  </div>

  <div class="back-footer">
    <div class="brand">
      <span class="brand__mark"></span>
      <div class="brand__name">PAW HAVEN</div>
      <div class="brand__sub">PET CARE</div>
    </div>
    <p class="contact-us">Contact Us</p>
    <div class="phone">
      <span class="phone__icon"><svg width="10" height="10" viewBox="0 0 24 24"><path fill="#fff" d="M6.6 10.8a15 15 0 0 0 6.6 6.6l2.2-2.2c.3-.3.7-.4 1-.2 1.1.4 2.3.6 3.6.6.6 0 1 .4 1 1V20c0 .6-.4 1-1 1A17 17 0 0 1 3 4c0-.6.4-1 1-1h3.5c.6 0 1 .4 1 1 0 1.3.2 2.5.6 3.6.1.3 0 .7-.2 1z"/></svg></span>
      <span class="phone__number">555-210-<span class="phone__word">BARK</span></span>
    </div>
    <div class="contacts">
      <span class="contact-line">www.pawhavenpets.com</span>
      <span class="contact-line">hello@pawhavenpets.com</span>
    </div>
  </div>
</section>

</body>
</html>
```